Box Truck Wrap

We need to create a design for our 26' box trucks. We want it to be very attention grabbing yet simple and we would like it to be modeled after our existing branding. The final deliverable needs to be 75DPI (Or more) at scale. The size of the wrap will be approximately 26' long and 8' tall. Colors are red white and blue. Please no stock images and we dpnt want any photos of people. Examples of other company trucks are included. We need one design for the side and also one for the back. Approx 7' x 8'

```html
<!DOCTYPE html>
<html lang="en">
<head>
<meta charset="utf-8">
<title>Highland Haulers – Box Truck Wrap Options</title>
<link rel="stylesheet" href="https://fonts.googleapis.com/css2?family=Josefin+Sans:wght@700&family=Open+Sans:wght@600;700&display=swap">
<style>
  :root{
    --navy:#1e1760;
    --red:#f50000;
    --maroon:#7d0f3c;
    --white:#ffffff;
    --paper:#ffffff;
  }
  html,body{margin:0;padding:0;width:1200px;height:1149px;overflow:hidden;background:var(--paper);}
  .wrap-sheet{display:block;width:1200px;height:1149px;}
  .brand-name{font-family:"Josefin Sans",sans-serif;font-weight:700;text-anchor:middle;}
  .brand-name--main{font-size:56px;letter-spacing:6px;}
  .brand-name--sub{font-size:32px;letter-spacing:17px;}
  .brand-name--main-sm{font-size:29px;letter-spacing:3px;}
  .brand-name--sub-sm{font-size:16px;letter-spacing:8px;}
  .contact{font-family:"Open Sans",sans-serif;fill:var(--white);}
  .contact--phone{font-size:26px;font-weight:600;}
  .contact--web{font-size:10.5px;font-weight:700;}
  .contact--end{text-anchor:end;}
  .contact--mid{text-anchor:middle;}
  .ridge-line{fill:none;stroke:var(--white);stroke-width:3;}
  .on-white{fill:var(--red);}
  .on-dark{fill:var(--white);}
</style>
</head>
<body>
<svg class="wrap-sheet" viewBox="0 0 1667 1600" preserveAspectRatio="none" xmlns="http://www.w3.org/2000/svg">
  <defs>
    <path id="star" d="M0,-26 L6.1,-8.4 L24.7,-8 L9.9,3.2 L15.3,21 L0,10.4 L-15.3,21 L-9.9,3.2 L-24.7,-8 L-6.1,-8.4Z"/>
    <linearGradient id="sky-red" x1="0" y1="0" x2="0" y2="1">
      <stop offset="0" stop-color="#f50000"/><stop offset="0.55" stop-color="#8d0a32"/><stop offset="1" stop-color="#5a1450"/>
    </linearGradient>
    <linearGradient id="hills-navy" x1="0" y1="0" x2="0" y2="1">
      <stop offset="0.3" stop-color="#1e1760"/><stop offset="1" stop-color="#7a0f3a"/>
    </linearGradient>
    <linearGradient id="hills-maroon" x1="0" y1="0" x2="0" y2="1">
      <stop offset="0" stop-color="#8a0f3a"/><stop offset="1" stop-color="#1e1760"/>
    </linearGradient>
    <linearGradient id="sky-navy-red" x1="0" y1="0" x2="0" y2="1">
      <stop offset="0" stop-color="#1e1760"/><stop offset="0.6" stop-color="#7d0f3c"/><stop offset="1" stop-color="#b00a22"/>
    </linearGradient>
    <linearGradient id="hills-navy-up" x1="0" y1="0" x2="0" y2="1">
      <stop offset="0.2" stop-color="#1e1760"/><stop offset="1" stop-color="#9a0c2c"/>
    </linearGradient>
  </defs>

  <!-- Side option 1 -->
  <g class="side-panel side-panel--navy">
    <rect x="168" y="162" width="937" height="288" fill="var(--navy)"/>
    <g fill="var(--white)">
      <use href="#star" transform="translate(644 212) scale(.65)" opacity=".45"/>
      <use href="#star" transform="translate(744 212) scale(.75)" opacity=".6"/>
      <use href="#star" transform="translate(844 212) scale(.85)" opacity=".75"/>
      <use href="#star" transform="translate(944 212) scale(.95)" opacity=".88"/>
      <use href="#star" transform="translate(1044 212) scale(1.05)"/>
    </g>
    <polyline class="ridge-line" points="168,365 203,365"/>
    <polyline class="ridge-line" points="566,365 580,365 665,316 765,343 845,306 883,325 962,271 1060,332 1105,320"/>
    <circle class="brand-dot" cx="387" cy="256" r="70" fill="var(--white)"/>
    <text class="brand-name brand-name--main on-dark" x="387" y="382">HIGHLAND</text>
    <text class="brand-name brand-name--sub on-dark" x="387" y="418">HAULERS</text>
    <text class="contact contact--phone contact--end" x="1063" y="385">(555) 014-2276</text>
    <text class="contact contact--web contact--end" x="1063" y="406">WWW.HIGHLANDHAULERSATX.COM</text>
  </g>

  <!-- Side option 2 -->
  <g class="side-panel side-panel--red">
    <rect x="168" y="494" width="937" height="288" fill="url(#sky-red)"/>
    <polygon points="168,655 215,700 590,705 665,648 765,673 845,638 883,655 962,603 1060,663 1105,652 1105,782 168,782" fill="url(#hills-navy)"/>
    <g fill="var(--navy)" stroke="var(--white)" stroke-width="3">
      <use href="#star" transform="translate(800 551)"/>
      <use href="#star" transform="translate(861 551)"/>
      <use href="#star" transform="translate(923 551)"/>
      <use href="#star" transform="translate(984 551)"/>
      <use href="#star" transform="translate(1045 551)"/>
    </g>
    <circle class="brand-dot" cx="387" cy="588" r="70" fill="var(--white)"/>
    <text class="brand-name brand-name--main on-dark" x="387" y="714">HIGHLAND</text>
    <text class="brand-name brand-name--sub on-dark" x="387" y="750">HAULERS</text>
    <text class="contact contact--phone contact--end" x="1063" y="728">(555) 014-2276</text>
    <text class="contact contact--web contact--end" x="1063" y="749">WWW.HIGHLANDHAULERSATX.COM</text>
  </g>

  <!-- Side option 3 -->
  <g class="side-panel side-panel--gable">
    <rect x="168" y="826" width="937" height="288" fill="var(--navy)"/>
    <polygon points="660,980 765,1005 845,970 883,987 962,935 1060,995 1105,984 1105,1114 660,1114" fill="url(#hills-maroon)"/>
    <polygon points="168,935 346,833 410,833 850,1114 168,1114" fill="var(--red)"/>
    <polygon points="168,977 386,845 810,1114 168,1114" fill="var(--white)"/>
    <g fill="var(--white)">
      <use href="#star" transform="translate(800 876)"/>
      <use href="#star" transform="translate(861 876)"/>
      <use href="#star" transform="translate(923 876)"/>
      <use href="#star" transform="translate(984 876)"/>
      <use href="#star" transform="translate(1045 876)"/>
    </g>
    <circle class="brand-dot" cx="387" cy="938" r="70" fill="var(--navy)"/>
    <text class="brand-name brand-name--main on-white" x="387" y="1063">HIGHLAND</text>
    <text class="brand-name brand-name--sub on-white" x="387" y="1099">HAULERS</text>
    <text class="contact contact--phone contact--end" x="1063" y="1043">(555) 014-2276</text>
    <text class="contact contact--web contact--end" x="1063" y="1064">WWW.HIGHLANDHAULERSATX.COM</text>
  </g>

  <!-- Side option 4 -->
  <g class="side-panel side-panel--gable-gradient">
    <rect x="168" y="1159" width="937" height="288" fill="url(#sky-navy-red)"/>
    <polygon points="660,1313 765,1338 845,1303 883,1320 962,1268 1060,1328 1105,1317 1105,1447 660,1447" fill="url(#hills-navy-up)"/>
    <polygon points="168,1268 346,1166 410,1166 850,1447 168,1447" fill="var(--red)"/>
    <polygon points="168,1310 386,1178 810,1447 168,1447" fill="var(--white)"/>
    <g fill="var(--white)">
      <use href="#star" transform="translate(800 1210) scale(.75)" opacity=".45"/>
      <use href="#star" transform="translate(861 1210) scale(.82)" opacity=".6"/>
      <use href="#star" transform="translate(923 1210) scale(.9)" opacity=".75"/>
      <use href="#star" transform="translate(984 1210) scale(.95)" opacity=".88"/>
      <use href="#star" transform="translate(1045 1210)"/>
    </g>
    <circle class="brand-dot" cx="387" cy="1272" r="70" fill="var(--navy)"/>
    <text class="brand-name brand-name--main on-white" x="387" y="1397">HIGHLAND</text>
    <text class="brand-name brand-name--sub on-white" x="387" y="1433">HAULERS</text>
    <text class="contact contact--phone contact--end" x="1063" y="1390">(555) 014-2276</text>
    <text class="contact contact--web contact--end" x="1063" y="1411">WWW.HIGHLANDHAULERSATX.COM</text>
  </g>

  <!-- Back door options -->
  <g class="back-panel back-panel--navy">
    <rect x="1240" y="162" width="252" height="288" fill="var(--navy)"/>
    <polyline class="ridge-line" points="1240,330 1285,350 1366,303 1448,350 1492,332"/>
    <circle class="brand-dot" cx="1366" cy="211" r="34" fill="var(--white)"/>
    <text class="brand-name brand-name--main-sm on-dark" x="1366" y="276">HIGHLAND</text>
    <text class="brand-name brand-name--sub-sm on-dark" x="1366" y="294">HAULERS</text>
    <text class="contact contact--phone contact--mid" x="1366" y="396">(555) 014-2276</text>
    <text class="contact contact--web contact--mid" x="1366" y="416">WWW.HIGHLANDHAULERSATX.COM</text>
  </g>

  <g class="back-panel back-panel--red">
    <rect x="1240" y="494" width="252" height="288" fill="url(#sky-red)"/>
    <polygon points="1240,662 1285,682 1366,635 1448,682 1492,664 1492,782 1240,782" fill="url(#hills-navy)"/>
    <circle class="brand-dot" cx="1366" cy="543" r="34" fill="var(--white)"/>
    <text class="brand-name brand-name--main-sm on-dark" x="1366" y="608">HIGHLAND</text>
    <text class="brand-name brand-name--sub-sm on-dark" x="1366" y="626">HAULERS</text>
    <text class="contact contact--phone contact--mid" x="1366" y="728">(555) 014-2276</text>
    <text class="contact contact--web contact--mid" x="1366" y="748">WWW.HIGHLANDHAULERSATX.COM</text>
  </g>

  <g class="back-panel back-panel--navy-maroon">
    <rect x="1240" y="826" width="252" height="288" fill="var(--navy)"/>
    <polygon points="1240,994 1285,1014 1366,967 1448,1014 1492,996 1492,1114 1240,1114" fill="url(#hills-maroon)"/>
    <circle class="brand-dot" cx="1366" cy="875" r="34" fill="var(--white)"/>
    <text class="brand-name brand-name--main-sm on-dark" x="1366" y="940">HIGHLAND</text>
    <text class="brand-name brand-name--sub-sm on-dark" x="1366" y="958">HAULERS</text>
    <text class="contact contact--phone contact--mid" x="1366" y="1060">(555) 014-2276</text>
    <text class="contact contact--web contact--mid" x="1366" y="1080">WWW.HIGHLANDHAULERSATX.COM</text>
  </g>

  <g class="back-panel back-panel--gradient">
    <rect x="1240" y="1158" width="252" height="288" fill="url(#sky-navy-red)"/>
    <polygon points="1240,1326 1285,1346 1366,1299 1448,1346 1492,1328 1492,1446 1240,1446" fill="url(#hills-navy-up)"/>
    <circle class="brand-dot" cx="1366" cy="1207" r="34" fill="var(--white)"/>
    <text class="brand-name brand-name--main-sm on-dark" x="1366" y="1272">HIGHLAND</text>
    <text class="brand-name brand-name--sub-sm on-dark" x="1366" y="1290">HAULERS</text>
    <text class="contact contact--phone contact--mid" x="1366" y="1392">(555) 014-2276</text>
    <text class="contact contact--web contact--mid" x="1366" y="1412">WWW.HIGHLANDHAULERSATX.COM</text>
  </g>
</svg>
</body>
</html>
```